Stationary Design For New Dynamic Company

Hi there we require stationary designed for our new company, we have used "Sketch Meadow" recently for our logo and were very impressed with all of the designers that contributed towards the final result.
What we require now is the following:
Letter head layout (A4)
Business Cards (5 people)
With Compliments slips
Envelopes
Email stationary
We would like to use our current logo design and I have included it for your use (JPEG is the one we have chosen and I have attached an EPS file for your use). Our company specializes in architectural cladding and our products are used by architects, builders and private clients, so we wish for the stationary to be suitable and attractive to our clientele.
I thank everyone in advance for your contributions.
Thank you to all that have provided your designs for this project, I apologize for not providing feedback as I have been away. I have looked at everyone's designs and they all look great and I will come back to those designers that I wish to have changes made sometime today.
Once again a big thank you to all involved.

```html
<!DOCTYPE html>
<html lang="en">
<head>
<meta charset="utf-8">
<title>Facadeform Stationery</title>
<link rel="stylesheet" href="https://fonts.googleapis.com/css2?family=Jost:wght@300;400;700&display=swap">
<style>
  :root {
    --stage: #d8d8d8;
    --paper: #ffffff;
    --navy: #161a50;
    --orange: #e8692c;
    --ink: #2b2b2b;
    --muted: #666a7a;
  }
  * { margin: 0; padding: 0; box-sizing: border-box; }
  html, body { width: 1200px; height: 800px; overflow: hidden; }
  body {
    background: var(--stage);
    font-family: "Jost", Arial, sans-serif;
    position: relative;
  }
  .sheet { position: absolute; overflow: hidden; }
  .paper { background: var(--paper); }
  .navy { background: var(--navy); }

  .wordmark {
    position: absolute;
    display: flex;
    align-items: center;
    gap: 6px;
    font-weight: 700;
    color: var(--navy);
    letter-spacing: -0.5px;
    white-space: nowrap;
  }
  .wordmark .mark-square {
    width: 0.7em; height: 0.7em;
    background: var(--orange);
    display: inline-block;
    flex: none;
  }
  .wordmark.on-navy { color: #ffffff; }

  .address {
    position: absolute;
    font-size: 8.5px;
    line-height: 11px;
    color: var(--muted);
    text-align: right;
  }

  /* compliments slip */
  .slip { left: 16px; top: 16px; width: 588px; height: 240px; }
  .slip .wordmark { right: 24px; top: 30px; font-size: 22px; }
  .slip .address { right: 24px; top: 66px; }
  .slip-title {
    position: absolute;
    right: 16px; top: 190px;
    font-size: 42px;
    font-weight: 300;
    color: var(--navy);
    letter-spacing: 0.5px;
    white-space: nowrap;
  }

  /* business cards */
  .card-front { left: 16px; top: 340px; width: 348px; height: 216px; }
  .card-front .wordmark { left: 172px; top: 22px; font-size: 20px; }
  .card-person { position: absolute; left: 236px; top: 76px; }
  .card-name { font-size: 13px; color: var(--navy); }
  .card-role { font-size: 9px; color: var(--muted); }
  .card-contact {
    position: absolute; left: 236px; top: 120px;
    font-size: 8.5px; line-height: 12px; color: var(--ink);
  }
  .card-front .address { left: 236px; top: 170px; text-align: left; color: var(--ink); }

  .card-back { left: 16px; top: 576px; width: 348px; height: 216px; }
  .card-back .wordmark { left: 162px; top: 56px; font-size: 20px; }

  /* C4 envelope (behind letterhead) */
  .envelope-c4 { left: 632px; top: 212px; width: 548px; height: 584px; }
  .envelope-c4 .wordmark { left: 170px; top: 418px; font-size: 22px; }

  /* DL envelope */
  .envelope-dl { left: 380px; top: 280px; width: 220px; height: 516px; }
  .envelope-dl .flap { position: absolute; left: 0; top: 0; width: 100%; height: 62px; background: var(--navy); }
  .envelope-dl .wordmark { right: 12px; top: 438px; font-size: 18px; }
  .envelope-dl .address { right: 12px; top: 468px; }

  /* letterhead */
  .letterhead { left: 752px; top: 16px; width: 432px; height: 584px; box-shadow: 0 0 3px rgba(0,0,0,0.15); }
  .letterhead .wordmark { right: 32px; top: 30px; font-size: 22px; }
  .letterhead .address { right: 32px; top: 66px; }
  .letter-body {
    position: absolute; left: 44px; top: 112px; width: 340px;
    font-size: 8.5px; line-height: 12.5px; color: var(--ink);
  }
  .recipient { margin-bottom: 26px; }
  .subject { font-weight: 700; margin-bottom: 12px; }
  .letter-body p { margin-bottom: 12px; text-align: justify; }
  .sign-off { position: absolute; left: 290px; top: 508px; font-size: 8.5px; color: var(--ink); }
  .sign-line { position: absolute; left: 290px; top: 548px; width: 70px; border-top: 1px solid var(--ink); }
</style>
</head>
<body>

  <section class="sheet paper slip">
    <div class="wordmark"><span class="mark-square"></span>FACADEFORM</div>
    <div class="address">Suite 4,<br>Linden Court Arcade<br>12 Elm Street, Melbourne</div>
    <h1 class="slip-title">WITH COMPLIMENTS</h1>
  </section>

  <section class="sheet paper card-front">
    <div class="wordmark"><span class="mark-square"></span>FACADEFORM</div>
    <div class="card-person">
      <div class="card-name">Mara Quinlan</div>
      <div class="card-role">director</div>
    </div>
    <div class="card-contact">m: 0400 123 456<br>mara@facadeform.com.au<br>www.facadeform.com.au</div>
    <div class="address">Suite 4, Linden Court Arcade<br>12 Elm Street, Melbourne</div>
  </section>

  <section class="sheet navy card-back">
    <div class="wordmark on-navy"><span class="mark-square"></span>FACADEFORM</div>
  </section>

  <section class="sheet navy envelope-c4">
    <div class="wordmark on-navy"><span class="mark-square"></span>FACADEFORM</div>
  </section>

  <section class="sheet paper envelope-dl">
    <div class="flap"></div>
    <div class="wordmark"><span class="mark-square"></span>FACADEFORM</div>
    <div class="address">Suite 4,<br>Linden Court Arcade<br>12 Elm Street, Melbourne</div>
  </section>

  <section class="sheet paper letterhead">
    <div class="wordmark"><span class="mark-square"></span>FACADEFORM</div>
    <div class="address">Suite 4,<br>Linden Court Arcade<br>12 Elm Street, Melbourne</div>
    <div class="letter-body">
      <div class="recipient">To:<br>Name Surname<br>Street Address</div>
      <div class="subject">Re: cladding proposal for the new arcade facade works</div>
      <p>Thank you for meeting with our team last week to discuss the facade package. We have reviewed the drawings and prepared an outline of panel options, finishes and lead times for your consideration.</p>
      <p>Our aluminium composite and fibre cement systems suit both commercial and residential work. Each option is tested for fire rating, weather resistance and long term colour stability. Samples of the three preferred finishes are enclosed with this letter, along with installation notes for your builder. We would be glad to arrange a site visit to confirm fixing details and measure the elevations before final pricing is issued.</p>
      <p>Please contact me directly with any questions. We look forward to working with you on this project.</p>
    </div>
    <div class="sign-off">Kind regards,</div>
    <div class="sign-line"></div>
  </section>

</body>
</html>
```